Lantern Marketing Group (LMG)

This is for my business cards. I want a Nice anfd Elegant Business Card to be Designed, Using more or less of the same colors of my logo that i have attached.i would like to have these business cards forever

Thank you

Thank you

Thank you

Contact Information for Business Card

Tobias Rennard
Lantern Marketing Group
C.(555) 214-6083
E-Mail. TRennard@lanternmgroup.example

Font styles to use
Serif
Sans Serif

Colors
d0dfed
cbcbcb
cee9f5

Requirements
Must have
• (LMG)
• Lantern Marketing Group
Nice to have
• 3D affects
Should not have
• Please try not using the flat version of the logo try and use the 3d version please

```html
<!DOCTYPE html>
<html lang="en">
<head>
<meta charset="utf-8">
<title>Lantern Marketing Group – Business Card</title>
<link href="https://fonts.googleapis.com/css2?family=Michroma&family=Roboto:wght@400&display=swap" rel="stylesheet">
<style>
  :root {
    --stage: #e4e7ea;
    --card-sky: #d6ebf6;
    --card-sky-deep: #c7e2f1;
    --card-white: #ffffff;
    --rule-grey: #cbcbcb;
    --brand-blue: #1f86c9;
    --brand-navy: #1565ad;
    --text-blue: #2a78bf;
    --mark-faint: rgba(31, 134, 201, 0.14);
    --shadow: rgba(30, 50, 70, 0.22);
  }
  * { box-sizing: border-box; margin: 0; padding: 0; }
  html, body {
    width: 1200px; height: 1000px; overflow: hidden;
    background: var(--stage);
  }
  .stage {
    width: 1200px; height: 1000px;
    display: flex; flex-direction: column;
    align-items: center; justify-content: center; gap: 70px;
  }
  .card {
    position: relative;
    width: 600px; height: 343px;
    border-radius: 22px;
    overflow: hidden;
    box-shadow: 0 10px 28px var(--shadow);
    background: linear-gradient(160deg, var(--card-sky) 0%, var(--card-sky-deep) 100%);
  }

  /* Front */
  .card-front .lower-band {
    position: absolute; left: 0; right: 0; bottom: 0; height: 118px;
    background: var(--card-white);
    border-top: 6px solid var(--rule-grey);
  }
  .card-front .faint-mark {
    position: absolute; left: 60px; top: 80px;
    width: 170px; height: 170px;
    background: var(--mark-faint);
  }
  .holder-name {
    position: absolute; left: 48px; top: 36px;
    font-family: "Michroma", sans-serif;
    font-size: 19px; letter-spacing: 1px;
    color: var(--brand-navy); text-transform: uppercase;
  }
  .holder-company {
    position: absolute; left: 48px; top: 68px;
    font-family: "Roboto", sans-serif; font-size: 15px;
    color: var(--text-blue);
  }
  .contact-list {
    position: absolute; left: 335px; top: 86px;
    list-style: none;
    font-family: "Roboto", sans-serif; font-size: 13px;
    color: var(--text-blue);
  }
  .contact-list li { display: flex; align-items: center; gap: 8px; height: 28px; }
  .contact-list svg { width: 20px; height: 20px; flex: none; }

  .wordmark {
    display: flex; align-items: center; gap: 12px;
    font-family: "Michroma", sans-serif;
    color: var(--brand-blue); text-transform: uppercase;
    line-height: 1.2;
  }
  .wordmark .wordmark-square { background: var(--brand-blue); flex: none; }
  .card-front .wordmark {
    position: absolute; right: 36px; bottom: 36px; font-size: 14px;
  }
  .card-front .wordmark-square { width: 42px; height: 42px; }

  /* Back */
  .card-back .faint-mark {
    position: absolute; right: 40px; top: 70px;
    width: 190px; height: 190px;
    background: var(--mark-faint);
  }
  .card-back .wordmark {
    position: absolute; left: 50%; top: 50%;
    transform: translate(-50%, -50%);
    font-size: 22px; white-space: nowrap;
  }
  .card-back .wordmark-square { width: 72px; height: 72px; }
</style>
</head>
<body>
<main class="stage">
  <section class="card card-front" aria-label="Business card front">
    <div class="faint-mark" aria-hidden="true"></div>
    <h1 class="holder-name">Tobias Rennard</h1>
    <p class="holder-company">Lantern Marketing Group C.</p>
    <ul class="contact-list">
      <li>
        <svg viewBox="0 0 20 20" aria-hidden="true"><circle cx="10" cy="10" r="9.5" fill="#2a78bf"/><path d="M6.5 5.5l2 0.2 0.8 2.3-1.2 1a6 6 0 0 0 2.9 2.9l1-1.2 2.3 0.8 0.2 2c-3.5 0.6-8.6-4.5-8-8z" fill="#fff"/></svg>
        (555) 214-6083
      </li>
      <li>
        <svg viewBox="0 0 20 20" aria-hidden="true"><circle cx="10" cy="10" r="9.5" fill="#2a78bf"/><rect x="5" y="6.5" width="10" height="7" fill="none" stroke="#fff" stroke-width="1.2"/><path d="M5 6.8l5 3.8 5-3.8" fill="none" stroke="#fff" stroke-width="1.2"/></svg>
        TRennard@lanternmgroup.example
      </li>
    </ul>
    <div class="lower-band"></div>
    <div class="wordmark">
      <span class="wordmark-square" aria-hidden="true"></span>
      <span class="wordmark-name">Lantern<br>Marketing Group</span>
    </div>
  </section>

  <section class="card card-back" aria-label="Business card back">
    <div class="faint-mark" aria-hidden="true"></div>
    <div class="wordmark">
      <span class="wordmark-square" aria-hidden="true"></span>
      <span class="wordmark-name">Lantern<br>Marketing Group</span>
    </div>
  </section>
</main>
</body>
</html>
```